Attorney Website Home Page Design Project

I am starting my law firm and I need a website design. I am going to be practicing in the field of personal injury, and I need a website design that conveys reliability and professionalism, but is still personable. This website will mostly be accessed by potential clients looking for information about me, and my potential clients are individual people, not businesses.

I have a logo that I just had designed by a designer on this site that I will be using. The colors used int he site should be complementary to the ones in that logo. Also, I have listed three websites that I want to base the overall look of my site on. This does NOT mean I want to copy them- instead, I am listing them for inspiration and to better convey what I am looking for.

Please use filler text and filler images for everything, and structure the menus as I have described below.

I will be taking this design- as a PSD file- and having it converted in to HTML, so I will need a perfect, multi-layered PSD file when completed.

I also will need a contact form that is consistent on every page.

Overall design on this site is up to you. See the attached logo files for inspiration on the color scheme. I am looking for a professional but personal website for my law firm. Check out the sites below for inspiration.

I. Websites for inspiration:

www.DorianWellsbyLaw.com THIS IS WHERE I WANT ABOUT 50% OF YOUR INSPIRATION TO COME FROM

www.QuillanPersonalInjury.com 25%

www.TopCounselNow.com 25%

I want all aspects of this site- menu panels and what not to be expandable and done in full uncompressed photoshop psd format so I can have them converted to html, and then in to a full site.

See the attached logo- the colors in it should direct the overall color scheme of the site.

I want you to use placeholder text and placeholder images- you can use white boxes with text in them that says what type of image should be used in its place. I also want a placeholder for a video on the home page.

II. Menu structure:

A. Main Menu and Submenu Items:

Our Purpose

What An Attorney Does

Why Choose Pembrook Attorneys

No Fee Guarantee

Cases We Handle (Below is a partial list- take the whole list from DorianWellsbyLaw.com

Auto Accidents

Slip and Fall Injuries

Dog Bites

Animal Bites

General Injury Cases

Your Case

How Are You Feeling?

What You Should Be Doing

Talk To Us

Contact Us

Target Market(s)

Injured people who need an attorney. Individuals, not companies.

Industry/Entity Type

Law Firm

Requirements
Must have
• Must be themed according to the websites I have listed and in line with my logo.

Must convey reliability, professionalism and warmth.

Must appeal to an individual person- I am practicing personal injury, not corporate or business law.

Must have one eye-catching item- "Contact Us Now to Get These Questions Answered:" with a 10 item numbered list of questions.
Should not have
• The site should not be cluttered or difficult to follow.

It should not be elitist or look like it is designed for corporate law.

```html
<!DOCTYPE html>
<html lang="en">
<head>
<meta charset="utf-8">
<title>Pembrook Attorneys – Home</title>
<link rel="stylesheet" href="https://fonts.googleapis.com/css2?family=Cinzel:wght@400;700&family=Open+Sans:wght@400;700&display=swap">
<style>
:root{
  --navy-deep:#04173f;
  --navy:#0c2a66;
  --navy-light:#1f4d9a;
  --gold:#e2b23a;
  --gold-light:#f3d37a;
  --gold-dark:#a77a16;
  --cream:#ece6d5;
  --cream-light:#f6f2e6;
  --ink:#1a1a1a;
  --white:#ffffff;
  --grey-dark:#3a3a3a;
}
*{box-sizing:border-box;margin:0;padding:0}
html,body{width:805px;height:1200px;overflow:hidden}
body{position:relative;background:var(--navy-deep);font-family:"Open Sans",Arial,sans-serif;color:var(--ink)}
.abs{position:absolute}
.header{left:0;top:0;width:805px;height:309px;background:radial-gradient(ellipse at 50% 20%,var(--navy-light) 0%,var(--navy) 45%,var(--navy-deep) 100%)}
.brand{left:160px;top:22px;width:217px;text-align:center;color:var(--white);font-family:"Cinzel",serif}
.brand-name{font-size:29px;font-weight:700;letter-spacing:1px;line-height:30px}
.brand-sub{font-size:8px;letter-spacing:4px;border-top:1px solid var(--white);margin-top:2px;padding-top:1px}
.connect{left:473px;top:12px;color:var(--gold-light);font-family:"Cinzel",serif;font-size:15px;letter-spacing:.5px}
.social{left:473px;top:37px;display:flex;gap:11px}
.social span{width:27px;height:29px;border-radius:5px;background:linear-gradient(var(--gold-light),var(--gold))}
.hero{left:143px;top:80px;width:517px;height:208px;background:var(--white);border-radius:8px;overflow:hidden;box-shadow:0 3px 8px rgba(0,0,0,.5)}
.hero-photo{position:absolute;left:0;top:0;width:380px;height:208px;background:linear-gradient(90deg,#c8c3bd 0%,#e5e1db 60%,rgba(255,255,255,0) 100%)}
.hero-title{position:absolute;left:270px;top:80px;font-family:"Cinzel",serif;color:var(--ink);line-height:21px}
.hero-title b{display:block;font-size:17px;font-weight:700}
.hero-title span{font-size:17px}
.hero-dots{position:absolute;left:441px;top:189px;display:flex;gap:3px}
.hero-dots i{width:7px;height:7px;border-radius:50%;background:var(--ink)}
.gold-rule{left:0;width:805px;height:5px;background:linear-gradient(var(--gold-light),var(--gold-dark))}
.main{left:0;top:314px;width:805px;height:509px;background:radial-gradient(ellipse at 50% 30%,var(--cream-light),var(--cream) 70%,#ddd5bf)}
.nav{left:116px;top:322px;width:571px;height:28px}
.nav-text{left:116px;top:322px;width:571px;height:24px;display:flex;justify-content:center;align-items:center;font-family:"Cinzel",serif;font-size:15px;color:var(--ink);gap:6px}
.card{width:166px;height:118px;top:365px;background:linear-gradient(var(--cream-light),#ddd6c3);border:1px solid #cfc6ae;border-radius:6px;box-shadow:0 2px 4px rgba(0,0,0,.3)}
.card-title{position:absolute;left:0;right:0;top:6px;text-align:center;font-family:"Cinzel",serif;color:#5b5448;font-size:21px;line-height:22px}
.card-title.stacked{top:4px;text-align:right;padding-right:10px;font-size:21px;line-height:20px;z-index:1}
.card-title.stacked small{display:block;font-size:10.5px;line-height:12px}
.card-img{position:absolute;left:5px;right:5px;top:36px;bottom:5px;border-radius:3px}
.learn{position:absolute;right:10px;bottom:10px;background:linear-gradient(var(--gold-light),var(--gold));font-family:"Cinzel",serif;font-weight:700;font-size:9px;padding:3px 6px;border-radius:3px;color:var(--ink)}
.intro{left:144px;top:500px;width:330px}
.intro h1{font-family:"Cinzel",serif;font-weight:700;font-size:17px;line-height:19px}
.intro h2{font-family:"Cinzel",serif;font-weight:400;font-size:17px;line-height:19px}
.intro p{font-size:10.4px;line-height:11.8px;margin-top:12px}
.panel{left:493px;width:167px;background:linear-gradient(var(--cream-light),#e3dcc7);border:1px solid #cfc6ae;border-radius:6px;box-shadow:0 2px 4px rgba(0,0,0,.3)}
.form{top:497px;height:152px;padding:5px 6px;font-size:7px}
.field{background:var(--white);border:1px solid #a9a08a}
.form label{display:block;margin-top:5px}
.form-row{display:flex;gap:6px}
.form-row div{flex:1}
.cta{margin:11px auto 0;width:148px;height:26px;border-radius:13px;background:linear-gradient(var(--gold-light),var(--gold));border:1px solid var(--gold-dark);font-size:9px;text-align:center;line-height:24px;white-space:nowrap;letter-spacing:-.1px}
.video{top:660px;height:153px}
.video h3{text-align:center;font-family:"Cinzel",serif;font-weight:400;font-size:15px;color:#4a443a;margin-top:10px}
.video-screen{position:absolute;left:6px;right:6px;top:36px;height:104px;background:var(--grey-dark)}
.footer{left:0;top:828px;width:805px;height:372px;background:linear-gradient(var(--navy),var(--navy-deep))}
.members-title{left:143px;top:840px;color:var(--white);font-family:"Cinzel",serif;font-size:15px}
.members{left:143px;top:863px;width:261px;height:46px;background:var(--white);border-radius:4px;display:flex;align-items:center;justify-content:space-between;padding:0 6px}
.members span{width:33px;height:33px;border-radius:50%;background:#9a8a5a;border:2px solid #444}
.col{top:926px;color:var(--white);font-family:"Cinzel",serif}
.col h4{font-weight:400;font-size:16.5px;line-height:19px;color:#dfe4f0}
.col ul{list-style:none;margin-top:30px;font-size:10px;line-height:11.2px}
.office p{font-size:12.5px;line-height:15px;margin-top:14px}
.office p:first-of-type{margin-top:24px}
</style>
</head>
<body>
<header class="abs header">
  <div class="abs brand"><div class="brand-name">Pembrook</div><div class="brand-sub">ATTORNEYS</div></div>
  <div class="abs connect">Connect us at</div>
  <div class="abs social"><span></span><span></span><span></span><span></span></div>
  <section class="abs hero">
    <div class="hero-photo" role="img" aria-label="Photo of an older client seated in a bright room"></div>
    <div class="hero-title"><b>LOREM IPSUM DOLOR</b><span>SIT AMET CONSECTETUR</span></div>
    <div class="hero-dots"><i></i><i></i><i></i><i></i><i></i><i></i></div>
  </section>
</header>
<div class="abs gold-rule" style="top:309px"></div>
<main class="abs main"></main>

<svg class="abs nav" viewBox="0 0 571 28" aria-hidden="true">
  <defs><linearGradient id="ribbon" x1="0" y1="0" x2="0" y2="1"><stop offset="0" stop-color="#f3d37a"/><stop offset="1" stop-color="#c9951f"/></linearGradient></defs>
  <polygon points="0,6 22,6 22,28 0,28 8,17" fill="#a77a16"/>
  <polygon points="571,6 549,6 549,28 571,28 563,17" fill="#a77a16"/>
  <rect x="14" y="0" width="543" height="24" fill="url(#ribbon)"/>
</svg>
<nav class="abs nav-text"><span>HOME</span>|<span>ABOUT US</span>|<span>CASE RESULT</span>|<span>TESTIMONIALS</span>|<span>CONTACT US</span></nav>

<article class="abs card" style="left:143px">
  <div class="card-title">Our Purpose</div>
  <div class="card-img" role="img" aria-label="Photo of courthouse columns" style="background:linear-gradient(#a89a82,#6d604c)"></div>
  <span class="learn">LEARN MORE</span>
</article>
<article class="abs card" style="left:320px">
  <div class="card-title stacked">What an<small>Attorney Does?</small></div>
  <div class="card-img" role="img" aria-label="Photo of a judge's gavel on a desk" style="top:38px;background:linear-gradient(135deg,#f2eee6,#bfb6a8)"></div>
  <span class="learn">LEARN MORE</span>
</article>
<article class="abs card" style="left:493px">
  <div class="card-title" style="font-size:17px">Why Chosen Us</div>
  <div class="card-img" role="img" aria-label="Photo of the legal team standing together" style="background:linear-gradient(#cfd3d8,#3d4350)"></div>
  <span class="learn">LEARN MORE</span>
</article>

<section class="abs intro">
  <h1>LOREM IPSUM DOLOR SIT AMET</h1>
  <h2>CONSECTETUR ADIPISICING ELIT</h2>
  <p>Lorem ipsum dolor sit amet, consectetur adipisicing elit, sed do eiusmod tempor incididunt ut labore et dolore magna aliqua. Ut enim ad minim veniam, quis nostrud exercitation ullamco laboris nisi ut aliquip ex ea commodo consequat. Duis aute irure dolor in reprehenderit in voluptate velit esse cillum dolore eu fugiat nulla pariatur. Excepteur sint occaecat cupidatat non proident, sunt in culpa qui officia deserunt mollit anim id est laborum</p>
  <p>Sed ut perspiciatis unde omnis iste natus error sit voluptatem accusantium doloremque laudantium, totam rem aperiam, eaque ipsa quae ab illo inventore veritatis et quasi architecto beatae vitae dicta sunt explicabo. Nemo enim ipsam voluptatem quia voluptas sit aspernatur aut odit aut fugit, sed quia consequuntur magni dolores eos qui ratione voluptatem sequi nesciunt. Neque porro quisquam est, qui dolorem ipsum quia dolor sit amet, consectetur, adipisci velit, sed quia non numquam eius modi tempora incidunt ut labore et dolore magnam aliquam quaerat voluptatem. Ut enim ad minima veniam, quis nostrum exercitationem ullam corporis suscipit laboriosam, nisi ut aliquid ex ea commodi consequatur? Quis autem vel eum iure reprehenderit qui in ea voluptate velit esse quam nihil molestiae consequatur, vel illum qui dolorem eum fugiat quo voluptas nulla pariatur</p>
</section>

<form class="abs panel form">
  <label style="margin-top:0">How can we help you?</label>
  <div class="field" style="height:40px;margin-top:3px"></div>
  <div class="form-row">
    <div><label>First name</label><div class="field" style="height:10px"></div></div>
    <div><label>Last Name</label><div class="field" style="height:10px"></div></div>
  </div>
  <div class="form-row">
    <div><label>Email</label><div class="field" style="height:10px"></div></div>
    <div><label>Phone number</label><div class="field" style="height:10px"></div></div>
  </div>
  <div class="cta">CLICK HERE TO <b>GET HELP NOW</b></div>
</form>

<section class="abs panel video">
  <h3>Watch Our Video</h3>
  <div class="video-screen">
    <svg width="155" height="104" viewBox="0 0 155 104" aria-label="Video placeholder"><circle cx="77" cy="52" r="18" fill="#5a5a5a"/><polygon points="71,42 71,62 87,52" fill="#3a3a3a"/></svg>
  </div>
</section>

<div class="abs gold-rule" style="top:823px"></div>
<footer class="abs footer"></footer>
<div class="abs members-title">Proud Member of</div>
<div class="abs members"><span></span><span></span><span></span><span></span><span></span><span></span></div>

<section class="abs col" style="left:143px">
  <h4>Practice Areas</h4>
  <ul style="margin-left:8px;margin-top:32px">
    <li>Aircraft Accident</li><li>Auto Accident</li><li>Boat Accident</li><li>Bus Accident</li><li>Defective Product</li><li>Dog Bite Injury</li><li>Drug Injury</li><li>Medical Malpractice</li><li>Motorcycle Accident</li><li>Premises Liability</li><li>Social Security Disability</li><li>Truck Accident</li><li>Workers' Compensation</li><li>Wrongful Death</li>
  </ul>
</section>
<section class="abs col" style="left:331px">
  <h4>Dangerous Drugs &amp;<br>Defective Products</h4>
  <ul style="margin-top:13px;margin-left:3px">
    <li>Glyvora</li><li>Antidepressant Birth Defects</li><li>Quitrel</li><li>Cold Therapy</li><li>Colon Cleansing Dangers</li><li>Orthalen Hip Recall</li><li>Gripseal</li><li>Ostevan</li><li>Rhythmex Liver Damage</li><li>Pain Patch</li><li>Clotrin</li><li>Stevens-Johnson Syndrome</li><li>Seizora</li><li>Transvaginal Mesh Failure</li><li>Workout Supplements</li><li>Lyra Birth Control</li><li>Serenex</li>
  </ul>
</section>
<section class="abs col office" style="left:537px">
  <h4>Main Office</h4>
  <p>327 W. Alder Street<br>Carson Falls, NV 89120</p>
  <p>Telephone:<br>(702) 555-0148</p>
  <p>Toll-Free:<br>(888) 555-0193</p>
  <p>Office Hours:<br>8:30 a.m. to 5:30 p.m.<br>(Pacific), M-F</p>
</section>
</body>
</html>
```